PSD website for property company

Please read the brief thoroughly.

We are looking for a new website for a property group that does property acquisitions, property development and property management.
They buy, build and lease core inner city industrial assets in Sydney, Australia.
They also invest in residential developments.

Site menu
- Home page
- Property – sub menus include – Leasing ; Projects ; Investments ; Property Management
- Capital and finance
- About
- Contact

They like this website
https://www.verlo.com.au/

They want the site to be clean, modern and bold.
They like few colors, even black and white is OK to submit

They have a logo and style guide and useable images here:
http://www.kumet.net/temp/PelorisWeb2019.zip
The zip file is also attached to this project.
We have supplied some images to give you an idea, but we will also require you to provide at least 3 extra images from stock photos.
Use your imagination.

I am expecting a lot of similar designs, so be aware the photos you choose will be really important.
They want really 3 good stock photos used and supplied without charge.
Please not too generic, I repeat the quality of the photos is important.
You may provide several photos (but not in multiple submissions please) and we will choose the best three to be provided.

The winner will be selected on a single home page design and required to provide;
All photos use in original format without charge
A second ‘standard page’ template design based on the winning home page design

```html
<!DOCTYPE html>
<html lang="en">
<head>
<meta charset="utf-8">
<title>Korvane — Property Group</title>
<link href="https://fonts.googleapis.com/css2?family=Montserrat:wght@500;600&family=Cabin:wght@500&family=Titillium+Web:ital,wght@1,300&family=Lato:wght@400&display=swap" rel="stylesheet">
<style>
:root{
  --accent:#d9974a;
  --ink:#1d1d1d;
  --body:#3a3a3a;
  --muted:#8a8a8a;
  --panel:#f5f5f5;
  --white:#ffffff;
}
*{margin:0;padding:0;box-sizing:border-box}
html,body{width:1200px;height:3745px;overflow:hidden;background:var(--white)}
body{position:relative;font-family:"Lato",sans-serif;color:var(--body)}
.abs{position:absolute}

/* hero */
.hero{left:0;top:0;width:1200px;height:600px;overflow:hidden;
  background:linear-gradient(180deg,#3d3a36 0%,#4a4440 40%,#3b2f2a 70%,#2e2a27 100%)}
.hero-frame{left:161px;top:93px;width:878px;height:410px;border:6px solid rgba(255,255,255,.16)}
.logo{font-family:"Montserrat",sans-serif;font-weight:600;letter-spacing:4px;color:var(--white);font-size:19px}
.site-logo{left:164px;top:27px}
.nav{right:161px;top:32px;display:flex;gap:22px;font-family:"Montserrat",sans-serif;font-weight:500;font-size:11px;color:var(--white);list-style:none}
.nav .active{color:var(--accent)}
.eyebrow{left:220px;top:188px;display:flex;align-items:center;gap:10px;font-family:"Montserrat",sans-serif;font-weight:600;font-size:12px;letter-spacing:1.5px;color:var(--white)}
.eyebrow::before{content:"";width:77px;height:1px;background:var(--white)}
.hero-title{left:220px;top:238px;font-family:"Montserrat",sans-serif;font-weight:600;font-size:44px;line-height:47px;letter-spacing:4px;color:var(--white)}
.hero-btn{left:220px;top:371px;width:170px;height:36px;background:var(--accent);border-radius:3px;display:flex;align-items:center;justify-content:center;gap:7px;font-family:"Montserrat",sans-serif;font-weight:500;font-size:10px;color:var(--white)}
.slides{left:0;top:238px;list-style:none;font-family:"Montserrat",sans-serif;color:rgba(255,255,255,.8);font-size:11px}
.slides li{display:flex;align-items:center;gap:10px;height:26px;letter-spacing:1px}
.slides li::before{content:"";width:14px;height:1px;background:rgba(255,255,255,.7)}
.slides li.current{font-size:19px;color:var(--white);font-weight:500;height:34px}
.slides li.current::before{width:26px;height:2px;background:var(--white)}
.side-pill{left:1110px;top:93px;width:130px;height:413px;background:var(--accent);border-radius:46px}
.pill-label{left:1110px;top:242px;width:92px;text-align:center;font-family:"Montserrat",sans-serif;font-size:8px;letter-spacing:1px;color:var(--white)}

/* intro */
.intro-logo{left:0;top:670px;width:1200px;text-align:center;color:var(--muted);font-size:17px}
.lead{left:165px;width:870px;text-align:center;font-family:"Titillium Web",sans-serif;font-style:italic;font-weight:300;font-size:25px;line-height:45px;color:var(--ink)}

/* feature rows */
.feature{left:161px;width:878px;height:570px;display:flex}
.feature-text{width:439px;background:var(--panel);padding:0 46px;display:flex;flex-direction:column;justify-content:center}
.feature-photo{width:439px;height:100%}
.feature h2,.section-title{font-family:"Cabin",sans-serif;font-weight:500;font-size:44px;line-height:53px;color:var(--ink)}
.feature h2{margin-bottom:28px}
.feature p{font-size:13px;line-height:22.5px;color:var(--body);margin-bottom:22px;width:350px}
.section-title{left:0;top:1598px;width:1200px;text-align:center}
.play{position:absolute;left:184px;top:228px}
</style>
</head>
<body>

<section class="abs hero" role="img" aria-label="Dusk photograph of a brick building with arched windows and a tree-lined street"></section>
<div class="abs hero-frame"></div>
<div class="abs logo site-logo">KORVANE</div>
<ul class="abs nav">
  <li>HOME</li><li>PROPERTY</li>
  <li class="active">[&nbsp; CAPITAL AND FINANCE ▾ ]</li>
  <li>ABOUT</li><li>CONTACT US</li>
</ul>
<ol class="abs slides">
  <li>01</li><li>02</li><li class="current">03</li><li>04</li><li>05</li>
</ol>
<div class="abs eyebrow">TRUST AND RECOMMENDED</div>
<h1 class="abs hero-title">LOREM IPSUM DOLOR &amp;<br>AMET NINGUN</h1>
<div class="abs hero-btn">
  <svg width="12" height="11" viewBox="0 0 12 11" fill="none" stroke="#fff" stroke-width="1"><path d="M1 4 6 1 11 4ZM2 5v4M4.5 5v4M7.5 5v4M10 5v4M1 10h10"/></svg>
  LOREM IPSUM DOLOR
</div>
<div class="abs side-pill"></div>
<svg class="abs" style="left:1140px;top:202px" width="32" height="32" viewBox="0 0 32 32" fill="none" stroke="#fff" stroke-width="1.2"><circle cx="16" cy="16" r="14"/><rect x="11" y="10" width="10" height="12"/><path d="M13 14h6M13 17h6"/></svg>
<div class="abs pill-label">PORTFOLIO</div>
<svg class="abs" style="left:1155px;top:284px" width="2" height="70"><rect width="1" height="70" fill="#fff"/></svg>
<svg class="abs" style="left:1147px;top:385px" width="18" height="13" viewBox="0 0 18 13" fill="none" stroke="#fff" stroke-width="1"><rect x=".5" y=".5" width="17" height="12"/><path d="M.5 .5 9 7l8.5-6.5"/></svg>

<div class="abs logo intro-logo">KORVANE</div>
<p class="abs lead" style="top:752px">With over 55 years in the industry and a highly skilled and specialised property team, we have established ourselves known as one of the most experienced, Australian owned, and fully integrated property active developers</p>

<article class="abs feature" style="top:961px">
  <div class="feature-text">
    <h2>Lorem Ipsum &amp;<br>Dolor</h2>
    <p>Lorem ipsum dolor amet gluten-free everyday carry vape, tbh taxidermy neutra yuccie filament bulb. Deep v pinboard disrupt knotgarden. Hot chicken neutra readymade loft blue bottle enamel pin vendo XOXO. Cray vinyl frazzled affogato, iceland paleo plaid pop-up health goth. Cred squid banh mi plaid, hammock church-key readymade</p>
    <p>Ennui kale chips vaporware lumbersexual, pok pok brunch health goth listicle copper mug kindling deep v truffle. Sriracha quinoa hammock truffle frazzled literally messenger bag sustainable before they sold out vape meggings</p>
    <p>Biodiesel pug celiac lomo, prism ethical typewriter vape brooklyn aesthetic succulents. Pork belly mustache synth, microdosing vexillologist listicle prism. Hella paleo snackwave shabby chic bicycle rights</p>
  </div>
  <div class="feature-photo" role="img" aria-label="Photograph of an orange-painted house with front steps and a leafy tree" style="background:linear-gradient(180deg,#9fb6cf 0%,#d7924a 35%,#c98236 65%,#5d6a3a 100%)"></div>
</article>

<h2 class="abs section-title">Biodiesel pug celiac lomo</h2>
<p class="abs lead" style="top:1683px">Affogato subway tile celiac cardigan. Drinking vinegar put any bird on it hoodie mustache celiac keytar raclette shaman keffiyeh shoreditch</p>

<article class="abs feature" style="top:1843px">
  <div class="feature-photo" role="img" aria-label="Photograph of a couple cooking together at a stove in a bright kitchen" style="background:linear-gradient(160deg,#eceae6 0%,#cfc8c0 45%,#8a6f64 75%,#3b3838 100%)"></div>
  <div class="feature-text">
    <h2>Dolor amet If</h2>
    <p>Ennui kale chips vaporware lumbersexual, pok pok brunch health goth listicle copper mug kindling deep v truffle. Sriracha quinoa hammock truffle frazzled literally messenger bag sustainable before they sold out vape meggings lorem ipsum dolor amet ningun postekam valar dohareis postedam if any wants brooklyn swag drinking winegar yolo valar morghulis and society is well known for more. Please stay updated with the news we provide</p>
  </div>
</article>

<article class="abs feature" style="top:2489px">
  <div class="feature-text">
    <h2>Slow-carb garden</h2>
    <p>Lorem ipsum dolor amet gluten-free everyday carry vape, tbh taxidermy neutra yuccie filament bulb. Deep v pinboard disrupt knotgarden. Hot chicken neutra readymade loft blue bottle enamel pin vendo XOXO. Cray vinyl frazzled affogato, iceland paleo plaid pop-up health goth. Cred squid banh mi plaid, hammock church-key readymade</p>
  </div>
  <div class="feature-photo" role="img" aria-label="Photograph of a dark study with a fur-draped chair, bookshelves and a model ship" style="background:linear-gradient(160deg,#5a3524 0%,#1f2336 45%,#2a2a3a 70%,#4a3020 100%)"></div>
</article>

<article class="abs feature" style="top:3135px;height:565px">
  <div class="feature-photo" style="position:relative;height:528px">
    <div role="img" aria-label="Rendering of a multi-storey brick apartment building on a street corner" style="width:100%;height:100%;background:linear-gradient(180deg,#c9d6e2 0%,#8a5e48 35%,#6b4433 70%,#3d2e28 100%)"></div>
    <svg class="play" width="72" height="72" viewBox="0 0 72 72"><circle cx="36" cy="36" r="34" fill="#d9974a" stroke="#fff" stroke-width="3"/><path d="M29 24 50 36 29 48Z" fill="#fff"/></svg>
  </div>
  <div class="feature-text" style="justify-content:flex-start;padding-top:78px">
    <h2>Dolor amet if</h2>
    <p>Ennui kale chips vaporware lumbersexual, pok pok brunch health goth listicle copper mug kindling deep v truffle. Sriracha quinoa hammock truffle frazzled literally messenger bag sustainable before they sold out vape meggings</p>
    <p>Affogato subway tile celiac cardigan. Drinking vinegar put a bird on it hoodie mustache celiac keytar raclette shaman keffiyeh shoreditch. Selvage hell of bicycle rights raw denim banjo readymade health goth aesthetic mumblecore master cleanse chambray wolf. Slow-carb garden 8-bit vendo tacos offal intelligentsia rhythm artisan pork belly gentrify woke echo park fam ramps. Yuccie deep v organic knotgarden succulents gastropub la crema tumeric chambray VHS fanny pack live-edge pop-up. Aesthetic viral typewriter seitan, polaroid forage thundercats</p>
  </div>
</article>

</body>
</html>
```